IT Company that provides secure IT solutions and services to our customers

We need business cards and a logo for a new IT Solutions company just created based in Kuala Lumpur, Malaysia. But will also be serving other countries in the region. We provide secure data, voice solutions on mobile platforms. Our first offering is encrypted voice and data solutions for ZUN, Pellovan, Quillet and Frondmoss devices.

Target Market(s)

large organizations Govt, Police, Defence, Anti-corruption, Legal, highly regulated industries such as Health-care, Financial, Banking, Insurance,

Industry/Entity Type

Information Technology

Contact Information for Business Card

VorlexIT (Logo - colour is ORVA blue)Rashid Nawfal Managing Director Kryption IT Sdn. Bhd.7th Floor, Block D, Wisma LPN,No.14 Jalan Seri Hamzani,58410, Kuala LumpurMalaysia

Font styles to use
Sans Serif

Colors
3176b5
ec1f27
fbed22

Requirements
Must have
• VorlexIT all in Blue like ORVA blue. A logo design perhaps a play of VI, K with a dangling T (colour can be any)
Nice to have
• I want a clean crisp card, not too busy, easy to read.

```html
<!DOCTYPE html>
<html lang="en">
<head>
<meta charset="utf-8">
<title>VorlexIT – Business Card</title>
<link rel="stylesheet" href="https://fonts.googleapis.com/css2?family=Roboto+Condensed:wght@400;700&display=swap">
<style>
  :root {
    --brand-blue: #3d80e6;
    --card-white: #ffffff;
    --page-bg: #ffffff;
  }
  * { margin: 0; padding: 0; box-sizing: border-box; }
  html, body {
    width: 1200px;
    height: 702px;
    overflow: hidden;
    background: var(--page-bg);
  }
  .business-card {
    position: relative;
    width: 1200px;
    height: 702px;
    background: var(--card-white);
    font-family: "Roboto Condensed", "Arial Narrow", sans-serif;
    color: var(--brand-blue);
  }
  .brand-mark {
    position: absolute;
    left: 196px;
    top: 188px;
    width: 190px;
    height: 190px;
    background: var(--brand-blue);
  }
  .brand-name {
    position: absolute;
    left: 90px;
    top: 496px;
    width: 402px;
    text-align: center;
    font-size: 76px;
    font-weight: 700;
    line-height: 1;
    letter-spacing: -1px;
  }
  .brand-tagline {
    position: absolute;
    left: 90px;
    top: 590px;
    width: 402px;
    text-align: center;
    font-size: 28px;
    font-weight: 400;
    letter-spacing: 0.5px;
    line-height: 1;
  }
  .contact {
    position: absolute;
    right: 103px;
    top: 82px;
    text-align: right;
    font-size: 38px;
    line-height: 56px;
    font-weight: 400;
    font-style: normal;
  }
  .contact-name {
    font-weight: 700;
    font-size: 39px;
  }
  .contact-group + .contact-group { margin-top: 54px; }
</style>
</head>
<body>
  <main class="business-card">
    <span class="brand-mark" aria-hidden="true"></span>
    <div class="brand-name">VORLEXIT</div>
    <div class="brand-tagline">MOBILE SECURE DATA &amp; VOICE</div>

    <address class="contact">
      <div class="contact-group">
        <div class="contact-name">Rashid Nawfal</div>
        <div class="contact-title">Managing Director</div>
      </div>
      <div class="contact-group">
        <div class="contact-phone">Tel (555) 418-2093</div>
        <div class="contact-email">email: rnawfal@vorlexit.com</div>
      </div>
      <div class="contact-group">
        <div>Sdn. Bhd. 7th Floor, Block D</div>
        <div>Wisma LPN, No. 14</div>
        <div>58410 Jalan Seri Hamzani</div>
        <div>Kuala Lumpur, Malaysia</div>
      </div>
    </address>
  </main>
</body>
</html>
```